Flyer Design for a Boston Therapeutic Clinic

I am a body therapist who needs a couple of flyers designed:
1. To fit half a page.
2. To fit a 5 inch by 3.5 inch flyer.
My practice is based in Boston, MA and my web site is:
www.LarchTessvik.Com
For the First half page:
A. Have my company's name and color shown as it appears on my web site (Larch Tessvik)
B. Have the following text: "Control your weight (This part should be emphasized) by balancing your nervous and digestive system through the Tessvik Method. The Tessvik Method, a technique developed by Dr. Mara. Tessvik, uses physical pressure to manipulate visceral tissue to bring back resiliency and proper functioning of the whole body."
Also helps with
-Constipation
-Bloating
-IBS
-eating disorders and overeating
Our practitioner is highly experienced. Please visit our web sites for reviews.
C. I would like to have a nice earthy feeling, something that feels "freeing" like open flowers, or an open land scape such as mountains or fields.
D. I also like the color blue, white, orange; perhaps if these colors can be integrated into the flyer, that would be great.
E. "Visit our web site LarchTessvik.com or call 786-555-0148"
The Smaller Flyer :
A.The smaller Flyer should also have my Company's name as shown on my web site (Larch Tessvik)
B.The following text: " Restore your body's natural resiliency and greatly reduce your physical pain through the Dr. Mara Tessvik Method of Structural Integration."
C. "Our practitioner is highly experienced and has a great reputation; visit our web site for reviews."
"Benefits:
"reduce aches and pains
reduce joint pain
reduce chronic muscular tension"
D, "feel better after the first session!"
E. if you could use a picture of me working on someone from my web site, that would be great.
F. I also like the colors white, orange and silver, for this one.
G. "Visit our web site LarchTessvik.com or call 786-555 0148"
I am very open minded,
I would like the flyer to evoke a sense of tranquility, professionalism, and simplicity. So if you have another angle you think would look good, then go for it! As long as it looks clean, professional and helpful.
Thanks a lot!
If you need any pictures from my web site, I have the original high resolution files that i can send.
Professionals and working men and women from ages 20-70
Clinic

```html
<!DOCTYPE html>
<html lang="en">
<head>
<meta charset="utf-8">
<title>Larch Tessvik Therapy — Flyer</title>
<link rel="stylesheet" href="https://fonts.googleapis.com/css2?family=Arimo:wght@400;700&family=Oswald:wght@400;500&family=Exo+2:wght@600;700&display=swap">
<style>
  :root {
    --page-bg: #e9e6e1;
    --orange: #e8622a;
    --amber: #f7941d;
    --gold: #ffc814;
    --yellow-text: #f5e21a;
    --ink: #2a2a2a;
    --grey-text: #5c5c5c;
    --panel-light: #ffffff;
    --panel-edge: #e4e4e4;
    --blue-top: #2a8fd0;
    --blue-bottom: #232a6b;
    --bullet: #d63a2a;
  }
  * { margin: 0; padding: 0; box-sizing: border-box; }
  html, body {
    width: 1200px; height: 883px; overflow: hidden;
    background: var(--page-bg);
  }
  .flyer {
    position: absolute; left: 10px; top: 24px;
    width: 1180px; height: 835px;
    background: radial-gradient(ellipse at 45% 40%, var(--panel-light) 0%, #f7f7f7 55%, var(--panel-edge) 100%);
    overflow: hidden;
    font-family: "Arimo", Arial, sans-serif;
    color: var(--ink);
  }
  .landscape {
    position: absolute; left: 0; top: 0; width: 1180px; height: 324px;
    background:
      linear-gradient(180deg, #dfe9f1 0%, #b8cbd9 22%, #7f8d96 42%, #a89584 58%, #c9683a 74%, #d5502a 86%, #e58a2f 100%);
  }
  .stripe {
    position: absolute; left: 0; width: 1180px;
    background: linear-gradient(90deg, var(--orange) 0%, var(--amber) 30%, var(--gold) 50%, var(--amber) 70%, var(--orange) 100%);
  }
  .stripe--under-photo { top: 324px; height: 11px; }
  .stripe--above-band { top: 686px; height: 11px; }
  .stripe--base { top: 810px; height: 25px; }
  .brand {
    position: absolute; right: 58px; top: 370px;
    font-family: "Arimo", Arial, sans-serif;
    font-weight: 400; font-size: 52px; letter-spacing: 0.5px;
    color: var(--orange); white-space: nowrap; line-height: 1;
  }
  .intro {
    position: absolute; left: 57px; top: 462px; width: 632px;
  }
  .intro__headline {
    font-family: "Oswald", "Arial Narrow", sans-serif;
    font-weight: 500; font-size: 39px; line-height: 1;
    color: var(--orange); margin-bottom: 10px;
  }
  .intro__body {
    font-size: 22.5px; line-height: 28.5px;
    text-align: justify; color: var(--ink);
  }
  .helps {
    position: absolute; left: 760px; top: 473px;
    font-size: 22.5px; color: var(--ink);
  }
  .helps__title { margin-bottom: 22px; line-height: 1; }
  .helps__list { list-style: none; }
  .helps__item {
    position: relative; padding-left: 22px;
    height: 36px; line-height: 26px;
  }
  .helps__item::before {
    content: ""; position: absolute; left: 2px; top: 9px;
    width: 10px; height: 10px; border-radius: 50%;
    background: radial-gradient(circle at 35% 35%, #f28a7a 0%, var(--bullet) 60%, #a32418 100%);
  }
  .contact-band {
    position: absolute; left: 0; top: 697px; width: 1180px; height: 113px;
    background: linear-gradient(180deg, var(--blue-top) 0%, #2a5ca3 45%, var(--blue-bottom) 100%);
    text-align: center;
  }
  .contact-band__reviews {
    position: absolute; left: 0; right: 0; top: 16px;
    font-size: 24px; color: var(--yellow-text); line-height: 1;
  }
  .contact-band__call {
    position: absolute; left: 0; right: 0; top: 54px;
    font-family: "Exo 2", Arial, sans-serif;
    font-weight: 700; font-size: 35px; letter-spacing: 0.8px;
    color: var(--amber); line-height: 1; white-space: nowrap;
  }
</style>
</head>
<body>
  <main class="flyer">
    <div class="landscape" role="img" aria-label="Open mountain landscape with autumn-coloured orange and red fields under a pale blue sky"></div>
    <div class="stripe stripe--under-photo"></div>

    <div class="brand">Larch Tessvik Therapy</div>

    <section class="intro">
      <h1 class="intro__headline">Control your weight</h1>
      <p class="intro__body">by balancing your nervous and digestive system through the Tessvik Method. The Tessvik Method, a technique developed by Dr. Mara. Tessvik, uses physical pressure to manipulate visceral tissue to bring back resiliency and proper functioning of the whole body.</p>
    </section>

    <section class="helps">
      <p class="helps__title">Also helps with</p>
      <ul class="helps__list">
        <li class="helps__item">Constipation</li>
        <li class="helps__item">Bloating</li>
        <li class="helps__item">IBS</li>
        <li class="helps__item">eating disorders and overeating</li>
      </ul>
    </section>

    <div class="stripe stripe--above-band"></div>
    <footer class="contact-band">
      <p class="contact-band__reviews">Our practitioner is highly experienced. Please visit our web sites for reviews.</p>
      <p class="contact-band__call">Visit our web site LarchTessvik.com or call 786-555-0148</p>
    </footer>
    <div class="stripe stripe--base"></div>
  </main>
</body>
</html>
```